KD Summit Fitness personal training needs a new Business Card design for 2016

Business Card design:
Our current business card is very plain
We are bringing on our first team member next year and thought its a perfect time to have a new face lift for our company!

We are a Personal Training business "KD Summit Fitness" who specializes in strength and conditioning / weightloss training,
We also run a yearly Bootcamp called "Ferocity Bootcamps", this is our Logo Design which we are looking for

The pink and blue in the logo are our business colours, how ever we don't want those colours to heavily dominate the card.

We are looking for a business card which is eye catching, and creative.

I am open to suggestions and any designs :)

Logo Design:

For our Logo Design we are looking for a bright, energetic logo, preferably a word logo which portrays strength and high intensity
If it has icon's etc in it thats fine again im open for suggestions :)
The Logo Design is for our Bootcamp which runs yearly
The bootcamp is called "Ferocity Bootcamp"

Target Market(s)

Age 20-40
Individuals who want to look great and have more energy

Industry/Entity Type

Business

Contact Information for Business Card

On the front
KD Summit Fitness Derwin Okoye Personal Training / Bootcamps / Pilates / Nutrition Healthy mind, Healthy body, Ultimate lifestyle < our slogan
Icons for the following
Email:
Mobile:
Facebook:
Instagram:

On the back we would like to include somewhere
"Show this card to receive 50% off your first 30min pt session"
"Valid to one user only"

Logo Text

Ferocity Bootcamp

Font styles to use
Serif

Colors
e34197
0255a3
000000
ffffff

Requirements
Must have
• - Icons for instagram, facebook, email and mobile phone
• - Slogan: Healthy mind, Healthy body, Ultimate lifestyle
• - What we offer: Personal Training , Bootcamps, Pilates, Nutrition
• - Logo
• -
Nice to have
• - Our 50% offer on the back
• - a place for a photo
Should not have
• - Pink and Blue everywhere

```html
<!DOCTYPE html>
<html lang="en">
<head>
<meta charset="utf-8">
<title>KD Summit Fitness – Business Card</title>
<link rel="stylesheet" href="https://fonts.googleapis.com/css2?family=Open+Sans:wght@400;600;800&display=swap">
<style>
  :root {
    --pink: #e34197;
    --blue: #0255a3;
    --card: #0d0d0d;
    --ink: #ffffff;
    --silver: #bfbfbf;
    --rule: #2e2e2e;
    --backdrop: #3a322d;
  }
  * { box-sizing: border-box; margin: 0; padding: 0; }
  html, body { width: 1200px; height: 900px; overflow: hidden; }
  body {
    background: var(--backdrop);
    font-family: "Open Sans", Arial, sans-serif;
    display: flex;
    align-items: center;
    justify-content: center;
    gap: 36px;
  }
  .card {
    position: relative;
    width: 550px;
    height: 314px;
    background: var(--card);
    color: var(--ink);
    box-shadow: 0 12px 30px rgba(0,0,0,.45);
  }
  .divider {
    position: absolute;
    top: 40px;
    width: 1px;
    background: var(--rule);
  }
  .brand {
    position: absolute;
    display: flex;
    flex-direction: column;
    align-items: center;
    gap: 10px;
    font-weight: 800;
    text-transform: uppercase;
    text-align: center;
    line-height: 1.05;
  }
  .brand-mark {
    width: 58px; height: 58px;
    border-radius: 50%;
  }
  .brand-name { font-size: 27px; letter-spacing: .5px; }
  .brand--front { left: 40px; top: 62px; width: 240px; }
  .brand--front .brand-mark { background: var(--blue); }
  .brand--front .brand-name { color: var(--blue); }
  .brand--back { left: 42px; top: 52px; width: 230px; }
  .brand--back .brand-mark { background: var(--silver); }
  .brand--back .brand-name { color: var(--silver); }

  /* front */
  .front .divider { left: 318px; height: 170px; }
  .holder {
    position: absolute; left: 340px; top: 48px;
    color: var(--pink); font-size: 19px; font-weight: 600;
  }
  .contacts {
    position: absolute; left: 340px; top: 88px;
    list-style: none; font-size: 14px; line-height: 24px;
  }
  .contacts li { display: flex; align-items: center; gap: 12px; }
  .contacts svg { width: 12px; height: 12px; flex: none; }
  .slogan {
    position: absolute; left: 40px; bottom: 34px;
    color: var(--pink); font-size: 18px; word-spacing: 2px;
  }

  /* back */
  .back .divider { left: 302px; height: 130px; }
  .offer-title {
    position: absolute; left: 326px; top: 36px;
    color: var(--pink); font-size: 15px; font-weight: 600;
  }
  .offer-list {
    position: absolute; left: 326px; top: 62px;
    list-style: none; font-size: 14px; line-height: 23px; font-weight: 600;
  }
  .offer-list li { display: flex; align-items: center; gap: 10px; }
  .offer-list li::before {
    content: ""; width: 8px; height: 8px; border-radius: 50%;
    background: var(--pink);
  }
  .promo {
    position: absolute; left: 0; right: 0; bottom: 56px;
    text-align: center; font-size: 13px; line-height: 19px;
  }
</style>
</head>
<body>

  <section class="card front" aria-label="Business card front">
    <div class="brand brand--front">
      <span class="brand-mark"></span>
      <span class="brand-name">KD Summit<br>Fitness</span>
    </div>
    <span class="divider"></span>
    <h1 class="holder">Derwin Okoye</h1>
    <ul class="contacts">
      <li>
        <svg viewBox="0 0 12 12" aria-label="Phone"><path fill="#e34197" d="M2.5 1h2l1 2.5-1.3 1a6 6 0 0 0 3.3 3.3l1-1.3L11 7.5v2c0 .8-.7 1.5-1.5 1.5A8.5 8.5 0 0 1 1 2.5C1 1.7 1.7 1 2.5 1z"/></svg>
        555 018 4420
      </li>
      <li>
        <svg viewBox="0 0 12 12" aria-label="Email"><rect x="1" y="2.5" width="10" height="7" fill="none" stroke="#e34197" stroke-width="1.2"/><path d="M1 2.5l5 4 5-4" fill="none" stroke="#e34197" stroke-width="1.2"/></svg>
        hello@kdsummitfit.com
      </li>
      <li>
        <svg viewBox="0 0 12 12" aria-label="Social page"><circle cx="6" cy="6" r="3.5" fill="#e34197"/></svg>
        social.kdsummitfit.com
      </li>
      <li>
        <svg viewBox="0 0 12 12" aria-label="Photo page"><rect x="2" y="2" width="8" height="8" fill="#e34197"/></svg>
        photos.kdsummitfit.com
      </li>
    </ul>
    <p class="slogan">Healthy Mind &nbsp;|&nbsp; Healthy Body &nbsp;|&nbsp; Ultimate Lifestyle</p>
  </section>

  <section class="card back" aria-label="Business card back">
    <div class="brand brand--back">
      <span class="brand-mark"></span>
      <span class="brand-name">KD Summit<br>Fitness</span>
    </div>
    <span class="divider"></span>
    <h2 class="offer-title">What we offer</h2>
    <ul class="offer-list">
      <li>Personal Training</li>
      <li>Bootcamps</li>
      <li>Pilates</li>
      <li>Nutrition</li>
    </ul>
    <p class="promo">Show this card to receive 50% off your first 30min pt session<br>Valid to one user only</p>
  </section>

</body>
</html>
```